Flyer-Design für Immobilienunternehmen
Zielgruppe
Verkauf von Immobilien und Grundstücken, Immobilienbewertung, Netzwerken in der Immobilienbranche
Private und gewerbliche Immobilien- und Grundstücksbesitzer, Erbengemeinschaften
Aufgabenstellung
Immobilienfachwirtin, Unternehmerin, Erfahrung,
Ich nehme mir Zeit für den Kunden

```html
<!DOCTYPE html>
<html lang="de">
<head>
<meta charset="utf-8">
<title>Lindner Immobilien – Flyer</title>
<link href="https://fonts.googleapis.com/css2?family=Didact+Gothic&family=Montserrat:wght@400;600;700&display=swap" rel="stylesheet">
<style>
:root{
  --green-dark:#5f8f3e;
  --green-mid:#7aab44;
  --green-light:#a6cc4a;
  --ink:#2d2d2d;
  --text:#555;
  --paper:#ffffff;
  --stage:#e4e4e4;
}
*{box-sizing:border-box;margin:0;padding:0}
html,body{width:1200px;height:2400px;overflow:hidden;background:var(--stage)}
body{position:relative;font-family:'Montserrat',sans-serif;color:var(--text)}
.spread{position:absolute;display:flex;box-shadow:0 8px 24px rgba(0,0,0,.15)}
.outside{left:110px;top:130px;width:1000px;height:990px}
.inside{left:110px;top:1310px;width:1000px;height:1030px}
.panel{position:relative;width:333.33px;height:100%;overflow:hidden;background:var(--paper)}
.green{background:linear-gradient(180deg,var(--green-dark),var(--green-mid) 60%,var(--green-light))}
.green-h{background:linear-gradient(90deg,var(--green-dark),var(--green-light))}
.photo{position:absolute;left:0;width:100%}
.heading{font-family:'Didact Gothic',sans-serif;text-transform:uppercase;letter-spacing:.5px}
.rule-title{display:flex;align-items:center;gap:10px;color:var(--ink);font-size:20px;margin:0 0 0 0}
.rule-title::before,.rule-title::after{content:"";flex:1;height:1px;background:var(--green-mid)}
.body-text{font-size:10.5px;line-height:1.35;color:var(--text)}
.body-text p{margin-bottom:10px}
.short-rule{width:34px;height:1px;background:var(--green-mid);margin:0 0 10px}
.band{position:absolute;left:0;width:100%;color:#fff;text-align:center;font-size:11px;line-height:1.3;padding:8px 20px}
.brand{font-family:'Didact Gothic',sans-serif;color:var(--green-dark);text-align:center;display:flex;align-items:center;justify-content:center;gap:10px}
.brand-dot{width:14px;height:14px;border-radius:50%;background:var(--green-mid)}
.brand-name{font-size:30px;letter-spacing:2px;text-transform:uppercase}
.web{font-family:'Didact Gothic',sans-serif;color:var(--ink);text-align:center;font-size:16px;letter-spacing:.5px}
/* outside */
.cover-quote{position:absolute;left:0;top:650px;width:100%;height:92px;padding:22px 26px;color:#fff;font-size:15px;line-height:1.3;transform:skewY(4deg);transform-origin:left}
.cover-quote span{display:block;transform:skewY(-4deg)}
.claim{color:#fff;font-size:28px;text-align:center;line-height:1.2}
.contact-box{position:absolute;left:32px;top:505px;width:275px;height:180px;border:1px solid rgba(255,255,255,.85);color:#fff;padding:0 20px}
.contact-box .lead{text-align:center;font-size:14px;line-height:1.3;margin-top:-10px;background:transparent}
.contact-line{display:flex;align-items:center;gap:12px;font-size:13px;margin-top:18px}
.contact-rule{width:140px;height:1px;background:rgba(255,255,255,.8);margin:14px auto 0}
.front-band{position:absolute;left:0;top:835px;width:100%;height:95px;transform:skewY(-6deg);color:#fff;text-align:center;font-size:26px;line-height:1.15;padding-top:16px}
/* inside */
.section{position:absolute;left:0;width:100%}
.section .icon{display:block;margin:0 auto 4px}
.step-title{font-family:'Didact Gothic',sans-serif;color:var(--green-dark);font-size:15px;text-transform:uppercase;display:flex;align-items:center;gap:8px;text-align:center}
.step-title::before,.step-title::after{content:"";flex:1;height:1px;background:var(--green-mid)}
.section h4{font-size:11px;font-weight:700;color:var(--ink);margin:18px 40px 10px 42px}
.section .body-text{margin:0 22px 0 42px;font-size:10.5px}
.middle{color:#fff;padding:0 28px}
.middle .title{font-family:'Didact Gothic',sans-serif;font-size:14px;display:flex;align-items:center;gap:10px;margin:60px -28px 0;justify-content:center}
.middle .title::before,.middle .title::after{content:"";flex:1;height:1px;background:rgba(255,255,255,.8)}
.middle .small{font-size:10px;line-height:1.35;color:rgba(255,255,255,.85)}
.steps{list-style:none;margin-top:16px}
.steps li{display:flex;align-items:center;gap:10px;font-size:10.5px;color:rgba(255,255,255,.9);height:32px}
.steps b{display:inline-flex;width:18px;height:18px;border-radius:50%;border-left:1px solid #fff;border-bottom:1px solid #fff;align-items:center;justify-content:center;font-weight:400;font-size:10px}
</style>
</head>
<body>

<!-- Outside spread -->
<section class="spread outside">
  <div class="panel">
    <div class="photo" role="img" aria-label="Foto: Maklerin am Schreibtisch im Büro" style="top:0;height:265px;background:linear-gradient(160deg,#d9dcd8,#b8b2a8 55%,#8a7a6e)"></div>
    <div style="position:absolute;top:258px;left:0;width:100%;height:14px;background:var(--green-mid);transform:skewY(-2deg)"></div>
    <h2 class="heading rule-title" style="position:absolute;top:298px;left:0;width:100%">Immobilienverkauf</h2>
    <div class="body-text" style="position:absolute;top:350px;left:24px;width:290px">
      <p>Eine Immobilie zu verkaufen, ob die eigene oder eine geerbte, geht nicht von heute auf morgen. Dessen ist man sich als Immobilienbesitzer bewusst. Ich verstehe mich als Partnerin an Ihrer Seite, die sich als lösungsorientierte Zuhörerin und Vermittlerin im Prozess Ihres Immobilienverkaufs sieht.</p>
      <div class="short-rule"></div>
      <p>Der Verkauf Ihrer Immobilie ist für mich nicht nur die Bewertung, das Erstellen eines Exposés und die Vertragsverhandlungen nach der Besichtigung. Mein Ziel ist es, gemeinsam mit Ihnen alle Aspekte des Verkaufs zu beleuchten, dazu braucht es Zeit und aktuelles Fachwissen. Beides können Sie von mir erwarten.</p>
      <div class="short-rule"></div>
      <p>Meine strukturierte Herangehensweise macht den Prozess für Sie transparenter. In jeder Phase des Verkaufs nehme ich mir die nötige Zeit, damit Sie danach sagen können:</p>
    </div>
    <div class="cover-quote green-h"><span>Mit Hilfe von Margit Lindner habe ich den Käufer gefunden, der passt.</span></div>
    <div class="photo" role="img" aria-label="Foto: Maklerin beim Unterschreiben von Unterlagen" style="top:740px;height:250px;background:linear-gradient(150deg,#cfd3d4,#a89c92 55%,#6f6a64)"></div>
  </div>

  <div class="panel">
    <div class="green" style="position:absolute;top:0;left:0;width:100%;height:750px"></div>
    <h2 class="heading claim" style="position:absolute;top:390px;width:100%">Ich nehme mir<br>Zeit für Sie!</h2>
    <div class="contact-box">
      <p class="lead"><span style="background:#6e9f40;padding:0 6px">Vereinbaren Sie einen</span><br>unverbindlichen persönlichen Gesprächstermin mit mir:</p>
      <div class="contact-rule"></div>
      <div class="contact-line">
        <svg width="20" height="20" viewBox="0 0 24 24" aria-hidden="true"><path d="M6 3l3 0 2 5-2 1.5c1 2.5 3 4.5 5.5 5.5L16 13l5 2v3c0 1-1 2-2 2C11 20 4 13 4 5c0-1 1-2 2-2z" fill="none" stroke="#fff" stroke-width="1.6"/></svg>
        <span>01234/56 78 900</span>
      </div>
      <div class="contact-line">
        <svg width="20" height="16" viewBox="0 0 24 18" aria-hidden="true"><rect x="1" y="1" width="22" height="16" fill="none" stroke="#fff" stroke-width="1.6"/><path d="M1 1l11 9 11-9" fill="none" stroke="#fff" stroke-width="1.6"/></svg>
        <span>info@lindner-immobilien</span>
      </div>
    </div>
    <div class="brand" style="position:absolute;top:860px;width:100%"><span class="brand-dot"></span><span class="brand-name">Lindner</span></div>
    <div class="brand" style="position:absolute;top:902px;width:100%;font-size:14px;letter-spacing:1px">— IMMOBILIEN —</div>
    <div class="web" style="position:absolute;top:940px;width:100%">WWW.LINDNER.IMMOBILIEN</div>
    <div style="position:absolute;bottom:0;left:0;width:100%;height:6px;background:var(--green-mid)"></div>
  </div>

  <div class="panel">
    <div style="position:absolute;top:0;width:100%;height:5px;background:var(--green-mid)"></div>
    <div class="brand" style="position:absolute;top:110px;width:100%"><span class="brand-dot"></span><span class="brand-name">Lindner</span></div>
    <div class="brand" style="position:absolute;top:152px;width:100%;font-size:14px;letter-spacing:1px">— IMMOBILIEN —</div>
    <div style="position:absolute;top:185px;left:0;width:100%;height:12px;background:var(--green-mid);transform:skewY(-1.5deg)"></div>
    <div class="photo" role="img" aria-label="Porträtfoto der Maklerin am Besprechungstisch" style="top:198px;height:545px;background:linear-gradient(160deg,#e4e8e6,#c7b9a9 50%,#7c6b5f)"></div>
    <svg style="position:absolute;top:520px;left:0" width="334" height="240" viewBox="0 0 334 240" aria-hidden="true"><path d="M0 200 Q80 250 200 200 T334 20 L334 60 Q290 180 200 220 Q90 260 0 215z" fill="var(--green-mid)"/></svg>
    <h2 class="heading" style="position:absolute;top:770px;left:18px;font-size:26px;color:var(--ink);transform:rotate(-6deg)">Immobilienverkauf</h2>
    <div class="front-band green-h heading">Ich nehme mir<br>Zeit für Sie!</div>
    <div class="web" style="position:absolute;top:930px;width:100%;transform:rotate(-6deg)">WWW.LINDNER.IMMOBILIEN</div>
    <div style="position:absolute;top:968px;left:0;width:100%;height:6px;background:var(--green-mid);transform:skewY(-6deg)"></div>
  </div>
</section>

<!-- Inside spread -->
<section class="spread inside">
  <div class="panel">
    <div class="section" style="top:30px">
      <svg class="icon" width="28" height="30" viewBox="0 0 28 30" aria-hidden="true"><circle cx="14" cy="13" r="8" fill="none" stroke="var(--green-mid)" stroke-width="2"/><rect x="10" y="22" width="8" height="5" fill="var(--green-mid)"/><path d="M14 9v6" stroke="var(--green-mid)" stroke-width="2"/></svg>
      <h3 class="step-title">1) Sich klar werden</h3>
      <h4>Die eigene Verkaufsbereitschaft auf den Prüfstand stellen</h4>
      <div class="body-text"><p>Neben der Klärung der Eigentumsverhältnisse, z.B. bei einer Erbengemeinschaft, geht es um Ihre Motivation und Verkaufsbereitschaft.</p><p>Haben Sie alle Möglichkeiten wie Renovierung und Vermietung durchdacht und eine Rentabilitätsrechnung erstellt? Ist ein Verkauf die richtige Entscheidung?</p></div>
    </div>
    <div class="band green-h" style="top:290px">Ich stelle Ihnen die passenden Fragen,<br>damit Sie sich klarwerden können.</div>
    <div class="section" style="top:365px">
      <svg class="icon" width="26" height="30" viewBox="0 0 26 30" aria-hidden="true"><rect x="3" y="2" width="18" height="25" fill="none" stroke="var(--green-mid)" stroke-width="2"/><path d="M7 9h10M7 14h10M7 19h6" stroke="var(--green-mid)" stroke-width="2"/></svg>
      <h3 class="step-title">2) Maklerauftrag</h3>
      <h4>Ihre Ziele entscheiden über die Art des Auftrags</h4>
      <div class="body-text"><p>Grundsätzlich können Sie sich entscheiden, ob Sie mich als Alleinmakler oder Nachweis- und Vermittlungsmakler beauftragen.</p><p>Ihr Vorteil bei der Alleinvermarktung ist, dass ich im festgelegten Zeitraum nachweisbar für Ihren Immobilienverkauf tätig werden muss.</p></div>
    </div>
    <div class="band green-h" style="top:612px">Die Transparenz durch die<br>Nachweisbarkeit gibt Ihnen Sicherheit.</div>
    <div class="section" style="top:675px">
      <svg class="icon" width="28" height="28" viewBox="0 0 24 24" aria-hidden="true"><path d="M12 2l3 7h7l-5.5 4.5 2 7.5L12 16.5 5.5 21l2-7.5L2 9h7z" fill="var(--green-mid)"/></svg>
      <h3 class="step-title">3) Immobilienbewertung</h3>
      <h4>Sich Zeit nehmen für Details</h4>
      <div class="body-text"><p>Basis für eine erfolgreiche Präsentation ist die Bewertung Ihrer Immobilie. Für diese nehme ich mir viel Zeit.</p><p>Neben einer Markteinschätzung fließen die baulichen Aspekte und die rechtlichen Gegebenheiten wie der Grundbuchauszug, die Bebauungsmöglichkeiten, die Vorgaben der Gemeinde/der Stadt und das Umfeld der Immobilie mit ein.</p></div>
    </div>
    <div class="band green-h" style="top:955px;transform:skewY(-3deg)">Gemeinsam arbeiten wir die Details für eine<br>erfolgreiche Verkaufs- &amp; Präsentationsstrategie aus.</div>
  </div>

  <div class="panel green middle">
    <h3 class="title">ZEIT FÜR TRANSPARENZ</h3>
    <p style="font-size:10.5px;font-weight:600;margin-top:28px">Wie schafft man Transparenz?</p>
    <p class="small">Aus meiner Sicht, indem man zuhört und vermittelt. Und das in jeder Phase des Immobilienverkaufs.</p>
    <p class="small" style="margin-top:18px">Für mich gibt es <b style="color:#fff">6 wesentliche Schritte</b> um das bestmögliche Verkaufsergebnis für Sie zu erreichen:</p>
    <div style="width:30px;height:1px;background:#fff;margin:14px 0 0"></div>
    <ol class="steps">
      <li><b>1</b>Sich klarwerden</li>
      <li><b>2</b>Richtige Art des Maklerauftrags festlegen</li>
      <li><b>3</b>Immobilienbewertung mit Detailbetrachtung</li>
      <li><b>4</b>Optimale Präsentation- und Verkaufsstrategie</li>
      <li><b>5</b>Besichtigung – den passenden Käufer finden</li>
      <li><b>6</b>Kaufvertrag aushandeln – Übergabe begleiten</li>
    </ol>
    <p class="small" style="margin-top:18px">Nehmen Sie sich die Zeit, diese Schritte gemeinsam mit mir <b style="color:#fff">„zu denken“</b>.</p>
    <p style="font-family:'Didact Gothic',sans-serif;font-size:15px;text-align:center;margin-top:22px;line-height:1.3">Der Prozess Ihres Verkaufs wird<br>so für Sie transparenter.</p>
    <div role="img" aria-label="Porträtfoto der Maklerin in schwarzer Kleidung" style="position:absolute;left:30px;right:0;bottom:0;height:300px;background:linear-gradient(180deg,rgba(0,0,0,0),#3a3a36 55%,#222)"></div>
  </div>

  <div class="panel">
    <div class="section" style="top:40px">
      <svg class="icon" width="30" height="28" viewBox="0 0 30 28" aria-hidden="true"><rect x="3" y="2" width="24" height="17" fill="none" stroke="var(--green-mid)" stroke-width="2"/><path d="M8 14l5-5 4 3 5-6M15 19v6M10 25h10" fill="none" stroke="var(--green-mid)" stroke-width="2"/></svg>
      <h3 class="step-title" style="line-height:1.2">4) Präsentation- und<br>Verkaufsstrategie</h3>
      <h4 style="margin-left:20px">Den potentiellen Käufer optimal ansprechen</h4>
      <div class="body-text" style="margin-left:20px"><p>Entsprechend der Zielgruppe für Ihre Immobilie arbeite ich die Präsentations- und Verkaufsstrategie auf Basis der Bewertung aus. Ein Eintrag in den bekannten Immobilienportalen reicht nicht immer. Ein ansprechendes Exposé, passende Außenwerbung, aber auch Diskretion wenn es notwendig ist, fließt in die Verkaufsstrategie mit ein.</p></div>
    </div>
    <div class="band green-h" style="top:285px">Die Bedürfnisse der potentiellen Käufer erkennen und Ihre Immobilien entsprechend präsentieren, ist der Schlüssel zum Verkaufserfolg.</div>
    <div class="section" style="top:370px">
      <svg class="icon" width="28" height="28" viewBox="0 0 28 28" aria-hidden="true"><circle cx="16" cy="11" r="8" fill="none" stroke="var(--green-mid)" stroke-width="2.5"/><path d="M10 17l-7 8" stroke="var(--green-mid)" stroke-width="3"/></svg>
      <h3 class="step-title">5) Besichtigungen</h3>
      <h4 style="margin-left:20px">Den passenden Käufer finden</h4>
      <div class="body-text" style="margin-left:20px"><p>Fingerspitzengefühl ist bei den Besichtigungen gefragt, denn in den wenigsten Fällen ist die Immobilie freistehend. Nicht nur die Kaufbereitschaft, sondern auch der Kaufwille durch eine entsprechende Zusage der Bank ist wichtig bei der Vorauswahl der potentiellen Käufer.</p><p>Das Ergebnis der Vorauswahl besprechen wir gemeinsam.</p></div>
    </div>
    <div class="band green-h" style="top:620px">Neben den Fakten ist mir wichtig, dass sie<br>nachdem Verkauf sagen können „das passt“.</div>
    <div class="section" style="top:685px">
      <svg class="icon" width="32" height="24" viewBox="0 0 32 24" aria-hidden="true"><path d="M2 8l7-4 7 4 7-4 7 4-4 6-8 6-8-6z" fill="var(--green-mid)"/></svg>
      <h3 class="step-title">6) Kaufvertrag aushandeln</h3>
      <h4 style="margin-left:20px">Übergabe begleiten</h4>
      <div class="body-text" style="margin-left:20px"><p>Zuhören, Lösungen finden, sich Zeit nehmen – der Ausarbeitung des Kaufvertrags gehört die meiste Sorgfalt.</p><p>Ich gebe Ihnen Antworten und zeige durch meine Erfahrung mit Notaren und auch Rechtsanwälten Möglichkeiten auf, um den Verkauf zu Ihrer vollsten Zufriedenheit abzuschließen.</p></div>
    </div>
    <div class="band green-h" style="top:960px;transform:skewY(3deg)">Nach der Schlüsselübergabe bin ich bei<br>Fragen weiterhin für Sie da.</div>
  </div>
</section>

</body>
</html>
```